The Lantern Protocol: A Practical Guide for Tending Old Orchards

This will be for both the hard cover and paperback version. A core theme of the book and what we want to cover to convey is the journey or transformation to "happiness". Concepts such as road/pathway, mountain top, sunrise, dark to bright colors, out-of-focus to in-focus, clouds parting, etc., all represent this idea. I am attaching a 1-page book summary for more information. I like the idea of the subtitle being in a gold seal, but that is not necessary. I am open to any designs, but it should at least be conceptually related to the book.

```html
<!DOCTYPE html>
<html lang="en">
<head>
<meta charset="utf-8">
<title>The Lantern Protocol — Book Cover</title>
<link rel="stylesheet" href="https://fonts.googleapis.com/css2?family=Poppins:wght@700&family=Playfair+Display:ital,wght@0,500;1,600&display=swap">
<style>
  :root {
    --band-blue: #074c8a;
    --sky-deep: #2d679a;
    --sky-mid: #8fb2cd;
    --cloud-white: #f5f8fb;
    --cloud-grey: #a9bfd0;
    --horizon-gold: #f2c45c;
    --horizon-glow: #f7e6b6;
    --field-green: #4e6d2a;
    --field-straw: #a8924c;
    --title-ink: #04192e;
    --subtitle-gold: #e6b748;
    --author-cream: #fdf8e6;
  }
  html, body {
    margin: 0;
    padding: 0;
    overflow: hidden;
    background: #ffffff;
  }
  .cover {
    position: relative;
    width: 800px;
    height: 1200px;
    overflow: hidden;
    background: var(--band-blue);
  }
  .cover-landscape {
    position: absolute;
    left: 0;
    top: 170px;
    width: 800px;
    height: 1030px;
    background: linear-gradient(
      to bottom,
      var(--band-blue) 0px,
      var(--sky-deep) 90px,
      var(--sky-mid) 170px,
      var(--cloud-white) 300px,
      var(--cloud-white) 440px,
      var(--cloud-grey) 560px,
      #c9d6df 640px,
      var(--horizon-glow) 700px,
      var(--horizon-gold) 735px,
      #6f7f5c 745px,
      var(--field-green) 800px,
      #6c7a35 880px,
      var(--field-straw) 1030px
    );
  }
  .subtitle {
    position: absolute;
    top: 84px;
    left: 0;
    width: 800px;
    margin: 0;
    text-align: center;
    font-family: "Poppins", sans-serif;
    font-weight: 700;
    font-size: 30px;
    line-height: 43px;
    letter-spacing: 3.6px;
    text-transform: uppercase;
    color: var(--subtitle-gold);
  }
  .title {
    position: absolute;
    top: 400px;
    left: 0;
    width: 800px;
    margin: 0;
    text-align: center;
    font-family: "Playfair Display", serif;
    color: var(--title-ink);
    font-weight: 500;
  }
  .title-article {
    display: block;
    font-style: italic;
    font-weight: 600;
    font-size: 84px;
    line-height: 84px;
    margin-right: 150px;
  }
  .title-line {
    display: block;
    font-size: 122px;
    line-height: 118px;
    letter-spacing: -1px;
  }
  .author {
    position: absolute;
    top: 1080px;
    left: 0;
    width: 800px;
    margin: 0;
    text-align: center;
    font-family: "Playfair Display", serif;
    font-weight: 500;
    font-size: 46px;
    letter-spacing: 2px;
    color: var(--author-cream);
  }
</style>
</head>
<body>
  <main class="cover">
    <div class="cover-landscape" role="img" aria-label="Photograph of a wide sky with parting clouds over a golden sunrise horizon and rolling grassy meadows with scattered trees"></div>
    <p class="subtitle">A Practical Guide for<br>Tending Old Orchards</p>
    <h1 class="title">
      <span class="title-article">The</span>
      <span class="title-line">Lantern</span>
      <span class="title-line">Protocol</span>
    </h1>
    <p class="author">Martin L. Haskell</p>
  </main>
</body>
</html>
```